Ledgerwise Code Works business card design.

We are a software development company that develop Software for finance companies and related industries.

We need a 2 sided business card designed. We have a new logo already designed (see attached eps and ai) We are after a clean simple corporate look. One side with just our logo, and the second side with our details.

Glen Marwick
Managing Director

Suite 5 Level 8, 147 Hollis Parade Sydney NSW 2000

Direct: +61 2 9374 6620
Mobile: +61 4 2873 5419
Email: glenm@lcw.net.au
Web: www.lcw.net.au

I have included 2 logo files an .ai and .eps. I noticed that the lines either side of the partners looks a bit jaggered and needs to be made sharper.

I would like to introduce a little colour somewhere rather than having it all black and white. But not over the top, keeping with a simple clean corporate look. Perhaps a light blue on some of the text?

If you have other ideas would be pleased to review

Regards

Glen M.

```html
<!DOCTYPE html>
<html lang="en">
<head>
<meta charset="utf-8">
<title>Ledgerwise Code Works – Business Card</title>
<link rel="stylesheet" href="https://fonts.googleapis.com/css2?family=Open+Sans:wght@400;600&family=Tinos&display=swap">
<style>
  :root {
    --backdrop: #6b6b6d;
    --card-black: #000000;
    --card-white: #ffffff;
    --paper-grey: #f1f1f1;
    --name-grey: #3a3a3a;
    --detail-grey: #8a8a8a;
    --accent-blue: #2a8fd0;
  }
  * { box-sizing: border-box; margin: 0; padding: 0; }
  html, body { width: 1200px; height: 873px; overflow: hidden; }
  body {
    background: var(--backdrop);
    display: flex;
    align-items: center;
    justify-content: center;
    gap: 60px;
    font-family: "Open Sans", Arial, sans-serif;
  }
  .card {
    position: relative;
    width: 520px;
    height: 297px;
    overflow: hidden;
    box-shadow: 0 8px 24px rgba(0,0,0,.35);
  }

  /* Brand mark: name set in text with a plain square */
  .brand { display: flex; align-items: center; gap: 10px; color: var(--card-white); }
  .brand-square { width: 22px; height: 22px; border: 2px solid var(--card-white); flex: none; }
  .brand-name {
    font-weight: 600;
    font-size: 13px;
    letter-spacing: .08em;
    text-transform: uppercase;
    line-height: 1.3;
  }

  /* Front */
  .card-front {
    background: var(--card-black);
    display: flex;
    align-items: center;
    justify-content: center;
  }
  .card-front .brand-name { font-size: 15px; }
  .card-front .brand-square { width: 28px; height: 28px; }

  /* Back */
  .card-back { background: var(--card-white); }
  .back-panel {
    position: absolute; top: 0; right: 0;
    width: 150px; height: 100%;
    background: var(--card-black);
    display: flex; align-items: flex-start; justify-content: center;
    padding-top: 40px;
  }
  .back-panel .brand { flex-direction: column; gap: 8px; text-align: center; }
  .back-panel .brand-name { font-size: 10px; }
  .back-edge {
    position: absolute; top: 0; right: 150px;
    width: 14px; height: 70px;
    background: var(--card-black);
  }
  .holder-name {
    position: absolute; left: 34px; top: 58px;
    font-family: "Tinos", "Times New Roman", serif;
    font-size: 34px;
    color: var(--name-grey);
    letter-spacing: .01em;
  }
  .role-band {
    position: absolute; left: 0; top: 126px;
    width: 370px; height: 28px;
    background: var(--card-black);
    color: var(--card-white);
    font-family: "Tinos", "Times New Roman", serif;
    font-size: 14px;
    padding-left: 34px;
    line-height: 28px;
  }
  .contact-list {
    position: absolute; left: 34px; top: 166px;
    list-style: none;
    font-size: 9.5px;
    color: var(--detail-grey);
  }
  .contact-list li { display: flex; align-items: center; gap: 8px; height: 17px; }
  .contact-icon { width: 12px; height: 12px; flex: none; }
  .footer-stripe {
    position: absolute; left: 0; bottom: 18px;
    width: 370px; height: 8px;
    background: var(--card-black);
  }
</style>
</head>
<body>

  <section class="card card-front" aria-label="Card front">
    <div class="brand">
      <span class="brand-square"></span>
      <span class="brand-name">Ledgerwise Code Works</span>
    </div>
  </section>

  <section class="card card-back" aria-label="Card back">
    <div class="back-edge"></div>
    <div class="back-panel">
      <div class="brand">
        <span class="brand-square"></span>
        <span class="brand-name">Ledgerwise<br>Code Works</span>
      </div>
    </div>

    <h1 class="holder-name">Glen Marwick</h1>
    <div class="role-band">Managing Director</div>

    <ul class="contact-list">
      <li>
        <svg class="contact-icon" viewBox="0 0 12 12"><rect width="12" height="12" rx="2" fill="var(--accent-blue)"/><path d="M2.5 4h7v4.5h-7z M2.5 4l3.5 2.6L9.5 4" fill="none" stroke="#fff" stroke-width=".9"/></svg>
        glenm@lcw.net.au
      </li>
      <li>
        <svg class="contact-icon" viewBox="0 0 12 12"><circle cx="6" cy="6" r="6" fill="var(--accent-blue)"/><path d="M4 3.2l1.2 1.5-.7.8c.5 1 1.2 1.7 2.1 2.1l.8-.7 1.5 1.2-.8 1C6 8.8 3.6 6.4 3.3 4z" fill="#fff"/></svg>
        +61 2 9374 6620
      </li>
      <li>
        <svg class="contact-icon" viewBox="0 0 12 12"><circle cx="6" cy="6" r="6" fill="var(--accent-blue)"/><rect x="4.2" y="2.6" width="3.6" height="6.8" rx=".6" fill="#fff"/><rect x="4.8" y="3.4" width="2.4" height="4.4" fill="var(--accent-blue)"/></svg>
        +61 4 2873 5419
      </li>
      <li>
        <svg class="contact-icon" viewBox="0 0 12 12"><circle cx="6" cy="6" r="6" fill="var(--accent-blue)"/><circle cx="6" cy="6" r="3.4" fill="none" stroke="#fff" stroke-width=".8"/><path d="M2.6 6h6.8M6 2.6c-1.6 2-1.6 4.8 0 6.8M6 2.6c1.6 2 1.6 4.8 0 6.8" fill="none" stroke="#fff" stroke-width=".7"/></svg>
        www.lcw.net.au
      </li>
      <li>
        <svg class="contact-icon" viewBox="0 0 12 12"><circle cx="6" cy="6" r="6" fill="var(--accent-blue)"/><path d="M6 2.4a2.4 2.4 0 0 1 2.4 2.4C8.4 6.6 6 9.6 6 9.6S3.6 6.6 3.6 4.8A2.4 2.4 0 0 1 6 2.4z" fill="#fff"/><circle cx="6" cy="4.8" r=".9" fill="var(--accent-blue)"/></svg>
        Suite 5 Level 8, 147 Hollis Parade Sydney NSW 2000
      </li>
    </ul>

    <div class="footer-stripe"></div>
  </section>

</body>
</html>
```